Travel video blogger needs website design

I need a website designed for my new travel video blog "Roaming Sparrow". I have only just started but need a website that is fairly simple and not too busy. I have a logo which I want on it (I have attached it to this project). I also want a link to all my other social medias on the main page (vidtrekhub, Snapwell and Palnook) and my videos as well. Here is a link to my vidtrekhub page for you to look at: https://www.vidtrekhub.net/channel/QRm4tZ8pWnE2HX57YKccd31v
As I have only just started and I am still trying to find my specific niche, again I need it to be sleek and simple that I can go in and change slightly here and there. I would like these pages on the website: About Me, Videos, Social Media, Blog, Gallery, contact me. for an example I like the look of www.theroamingkinfolk.net website.

I already have the domain and I am with Harborweb with pagecraftr.org. I just want to spend my time getting better and learning about videos then trying to create a website (I am a bit of a perfectionist when I try to do something).

Target Market(s)

Young Adults (majority females) between the ages of 18 and 30 with an interest in travelling.

Industry/Entity Type

Travel Industry

Number of Pages Required

1 page

Colors

Designer to choose colors to be used in the design.

Requirements
Must have
• A like to my Snapwell, Palnook and vidtrekhub channels on the home page
• Must be a nice, simple design
• Must have my logo on the front and name "Roaming Sparrow"
Nice to have
• A nice light, bright coloured theme
Should not have
• A dark coloured theme

```html
<!DOCTYPE html>
<html lang="en">
<head>
<meta charset="utf-8">
<title>Roaming Sparrow — Travel Video Blog</title>
<link rel="stylesheet" href="https://fonts.googleapis.com/css2?family=Montserrat:wght@400;600;700&family=Open+Sans:wght@400;600&display=swap">
<style>
  :root {
    --ink: #2b2b2b;
    --muted: #8a8a8a;
    --faint: #b9b9b9;
    --line: #e6e6e6;
    --paper: #ffffff;
    --card: #f7f7f7;
    --white: #ffffff;
    --sky-warm: #e9d6c3;
    --sky-cool: #b8c3cf;
    --sea: #3f78a8;
  }
  * { margin: 0; padding: 0; box-sizing: border-box; }
  a, a:visited { color: inherit; text-decoration: none; }
  html, body { width: 809px; height: 1200px; overflow: hidden; background: var(--paper); }
  body { position: relative; font-family: "Open Sans", Arial, sans-serif; color: var(--ink); }

  /* Header */
  .site-header { position: absolute; left: 165px; top: 14px; width: 480px; height: 60px; }
  .brand { position: absolute; left: 0; top: 0; width: 110px; text-align: center; display: block; color: var(--ink); }
  .brand-mark { display: block; width: 34px; height: 34px; margin: 0 auto 5px; border-radius: 50%; background: var(--ink); }
  .brand-name { display: block; font-family: "Montserrat", Arial, sans-serif; font-weight: 700; font-size: 9px; letter-spacing: 1.2px; color: var(--ink); text-transform: uppercase; white-space: nowrap; }
  .social-top { position: absolute; right: 0; top: 14px; display: flex; gap: 5px; }
  .social-dot { width: 13px; height: 13px; border-radius: 50%; background: var(--ink); display: block; }
  .main-nav { position: absolute; right: 0; top: 44px; display: flex; gap: 14px; }
  .main-nav a { font-family: "Montserrat", Arial, sans-serif; font-size: 6.5px; letter-spacing: .6px; color: var(--muted); text-transform: uppercase; }
  .main-nav a.is-active { color: var(--ink); font-weight: 600; }

  /* Hero */
  .hero { position: absolute; left: 170px; top: 81px; width: 470px; height: 162px; background: linear-gradient(100deg, var(--sky-cool) 0%, #d9cfc8 45%, var(--sky-warm) 75%, #f3e4cf 100%); }

  /* Welcome */
  .welcome { position: absolute; left: 170px; top: 256px; width: 470px; text-align: center; }
  .welcome-kicker { font-family: "Montserrat", Arial, sans-serif; font-size: 8px; font-weight: 600; letter-spacing: 1px; text-transform: uppercase; }
  .welcome-title { font-family: "Montserrat", Arial, sans-serif; font-size: 12px; font-weight: 700; letter-spacing: 2px; text-transform: uppercase; margin-top: 3px; }
  .welcome-text { font-size: 6.5px; line-height: 10px; color: var(--muted); margin: 6px auto 0; width: 440px; }

  /* Destinations */
  .destinations { position: absolute; left: 170px; top: 336px; width: 470px; display: grid; grid-template-columns: repeat(3, 1fr); gap: 9px 10px; }
  .destination { position: relative; height: 98px; display: flex; align-items: center; justify-content: center; }
  .destination-name { position: relative; font-family: "Montserrat", Arial, sans-serif; font-weight: 700; font-size: 14px; letter-spacing: 1.5px; color: var(--white); text-transform: uppercase; }
  .dest-santorini { background: linear-gradient(160deg, #9fb6cc, #5c7a99); }
  .dest-paris { background: linear-gradient(160deg, #a9b7c6, #6a7686); }
  .dest-india { background: linear-gradient(160deg, #c7c2bb, #8f8a83); }
  .dest-turkey { background: linear-gradient(160deg, #b7c2cc, #7d8790); }
  .dest-england { background: linear-gradient(160deg, #c4c9cf, #7e8893); }
  .dest-germany { background: linear-gradient(160deg, #8fb0d6, #55708c); }

  /* Section titles */
  .section-title { position: absolute; left: 170px; width: 470px; text-align: center; font-family: "Montserrat", Arial, sans-serif; font-size: 9.5px; font-weight: 600; letter-spacing: 1.2px; text-transform: uppercase; }
  .videos-title { top: 570px; }
  .blog-title { top: 832px; }

  /* Videos */
  .videos { position: absolute; left: 170px; top: 600px; width: 470px; height: 186px; display: grid; grid-template-columns: 232px 1fr 1fr; grid-template-rows: 1fr 1fr; gap: 5px; }
  .video { position: relative; display: flex; align-items: center; justify-content: center; }
  .video-feature { grid-row: 1 / 3; background: linear-gradient(180deg, #c9dbe8 0%, #8fb4cf 55%, var(--sea) 100%); }
  .video-sunset { background: linear-gradient(180deg, #e0a36a, #6b5a78); }
  .video-coast { background: linear-gradient(180deg, #7fa7c4, #3d5f7a); }
  .video-night { background: linear-gradient(180deg, #4a4f6e, #8a6d6a); }
  .video-all { background: linear-gradient(180deg, #6e8796, #36444d); }
  .play-icon { width: 20px; height: 20px; }
  .video-feature .play-icon { width: 26px; height: 26px; }
  .all-videos { font-family: "Montserrat", Arial, sans-serif; font-size: 7px; font-weight: 600; letter-spacing: 1px; color: var(--white); text-transform: uppercase; }

  /* Blog */
  .blog { position: absolute; left: 170px; top: 858px; width: 470px; display: grid; grid-template-columns: repeat(3, 1fr); gap: 10px; }
  .post { background: var(--card); }
  .post-image { height: 70px; }
  .post-image-1 { background: linear-gradient(160deg, #dfe4e6, #a7b6bd); }
  .post-image-2 { background: linear-gradient(160deg, #9fd0e0, #d9c9a4); }
  .post-image-3 { background: linear-gradient(180deg, #7ec8e6, #4fa7c9 60%, #e9dcc0); }
  .post-body { padding: 7px 8px 8px; }
  .post-title { font-family: "Montserrat", Arial, sans-serif; font-size: 8px; font-weight: 700; line-height: 11px; }
  .post-excerpt { font-size: 6px; line-height: 9px; color: var(--muted); margin-top: 3px; }
  .post-meta { display: flex; gap: 14px; margin-top: 8px; font-size: 5.5px; color: var(--faint); }
  .post-meta span::before { content: ""; display: inline-block; width: 4px; height: 4px; border-radius: 50%; background: var(--faint); margin-right: 3px; vertical-align: middle; }

  /* Footer */
  .site-footer { position: absolute; left: 170px; top: 1046px; width: 470px; border-top: 1px solid var(--line); text-align: center; padding-top: 16px; }
  .site-footer .brand { position: static; width: 110px; margin: 0 auto; }
  .footer-nav { display: flex; justify-content: center; gap: 14px; margin-top: 14px; }
  .footer-nav a { font-family: "Montserrat", Arial, sans-serif; font-size: 6px; letter-spacing: .6px; color: var(--muted); text-transform: uppercase; }
  .social-bottom { display: flex; justify-content: center; gap: 6px; margin-top: 10px; }
  .copyright { font-size: 5.5px; color: var(--faint); margin-top: 8px; }
</style>
</head>
<body>

<header class="site-header">
  <a class="brand" href="#">
    <span class="brand-mark"></span>
    <span class="brand-name">Roaming Sparrow</span>
  </a>
  <div class="social-top">
    <a class="social-dot" href="#" aria-label="Snapwell"></a>
    <a class="social-dot" href="#" aria-label="Palnook"></a>
    <a class="social-dot" href="#" aria-label="vidtrekhub"></a>
  </div>
  <nav class="main-nav">
    <a class="is-active" href="#">About Me</a>
    <a href="#">Videos</a>
    <a href="#">Social Media</a>
    <a href="#">Blog</a>
    <a href="#">Gallery</a>
    <a href="#">Contact Me</a>
  </nav>
</header>

<div class="hero" role="img" aria-label="Traveller seated on a hilltop looking over a misty valley at sunrise"></div>

<section class="welcome">
  <p class="welcome-kicker">Welcome to</p>
  <h1 class="welcome-title">Roaming Sparrow</h1>
  <p class="welcome-text">Roaming Sparrow follows one young traveller across coasts, cities and mountain roads. Here you will find short travel films, honest guides and simple tips for planning your next trip, shared from the road as each new story unfolds.</p>
</section>

<section class="destinations">
  <a class="destination dest-santorini" href="#" role="img" aria-label="Whitewashed village above the sea in Santorini"><span class="destination-name">Santorini</span></a>
  <a class="destination dest-paris" href="#" role="img" aria-label="Paris skyline"><span class="destination-name">Paris</span></a>
  <a class="destination dest-india" href="#" role="img" aria-label="Palace in India"><span class="destination-name">India</span></a>
  <a class="destination dest-turkey" href="#" role="img" aria-label="Mosque domes in Turkey"><span class="destination-name">Turkey</span></a>
  <a class="destination dest-england" href="#" role="img" aria-label="Clock tower in England"><span class="destination-name">England</span></a>
  <a class="destination dest-germany" href="#" role="img" aria-label="Castle in Germany"><span class="destination-name">Germany</span></a>
</section>

<h2 class="section-title videos-title">Recent Videos</h2>
<section class="videos">
  <a class="video video-feature" href="#" role="img" aria-label="Tall ship sailing on blue water">
    <svg class="play-icon" viewBox="0 0 24 24"><path d="M7 4l13 8-13 8z" fill="#fff"/></svg>
  </a>
  <a class="video video-sunset" href="#" role="img" aria-label="Sunset over a lake">
    <svg class="play-icon" viewBox="0 0 24 24"><path d="M7 4l13 8-13 8z" fill="#fff"/></svg>
  </a>
  <a class="video video-coast" href="#" role="img" aria-label="Rocky coastline">
    <svg class="play-icon" viewBox="0 0 24 24"><path d="M7 4l13 8-13 8z" fill="#fff"/></svg>
  </a>
  <a class="video video-night" href="#" role="img" aria-label="City lights at night">
    <svg class="play-icon" viewBox="0 0 24 24"><path d="M7 4l13 8-13 8z" fill="#fff"/></svg>
  </a>
  <a class="video video-all" href="#" role="img" aria-label="Mountain lake view"><span class="all-videos">All Videos</span></a>
</section>

<h2 class="section-title blog-title">Latest Blog</h2>
<section class="blog">
  <article class="post">
    <div class="post-image post-image-1" role="img" aria-label="Travel planning flat lay with map and camera"></div>
    <div class="post-body">
      <h3 class="post-title">Lorem Ipsum is not simply</h3>
      <p class="post-excerpt">A short note from the road with tips, views and moments worth sharing.</p>
      <p class="post-meta"><span>Travel</span><span>2 Comments</span></p>
    </div>
  </article>
  <article class="post">
    <div class="post-image post-image-2" role="img" aria-label="Vintage camper van on a beach road"></div>
    <div class="post-body">
      <h3 class="post-title">Lorem Ipsum is not simply</h3>
      <p class="post-excerpt">A short note from the road with tips, views and moments worth sharing.</p>
      <p class="post-meta"><span>Travel</span><span>2 Comments</span></p>
    </div>
  </article>
  <article class="post">
    <div class="post-image post-image-3" role="img" aria-label="Cocktail glass on a tropical beach"></div>
    <div class="post-body">
      <h3 class="post-title">Lorem Ipsum is not simply</h3>
      <p class="post-excerpt">A short note from the road with tips, views and moments worth sharing.</p>
      <p class="post-meta"><span>Travel</span><span>2 Comments</span></p>
    </div>
  </article>
</section>

<footer class="site-footer">
  <a class="brand" href="#">
    <span class="brand-mark"></span>
    <span class="brand-name">Roaming Sparrow</span>
  </a>
  <nav class="footer-nav">
    <a href="#">About Me</a>
    <a href="#">Videos</a>
    <a href="#">Social Media</a>
    <a href="#">Blog</a>
    <a href="#">Gallery</a>
    <a href="#">Contact Me</a>
  </nav>
  <div class="social-bottom">
    <a class="social-dot" href="#" aria-label="Snapwell"></a>
    <a class="social-dot" href="#" aria-label="Palnook"></a>
    <a class="social-dot" href="#" aria-label="vidtrekhub"></a>
  </div>
  <p class="copyright">© 2018 Roaming Sparrow. All rights reserved.</p>
</footer>

</body>
</html>
```